hfdhddfgfhfghfghgfhfhfhgfhfhfh

Industry/Entity Type

Painting

Logo Text

TOLVEN Painting

Logo styles of interest
Wordmark Logo
Requirements
Should not have
• Paintbrushes or rollers etc....

```html
<!DOCTYPE html>
<html lang="en">
<head>
<meta charset="utf-8">
<title>TOLVEN Painting – Business Card</title>
<link rel="stylesheet" href="https://fonts.googleapis.com/css2?family=Oswald:wght@400;500&family=Roboto:wght@400;500&display=swap">
<style>
  :root {
    --page-bg: #ffffff;
    --page-border: #e6e6e6;
    --card-border: #d9d9d9;
    --ink: #231f20;
    --brand-blue: #0f86d2;
    --panel-dark: #0a7cc4;
    --panel-light: #1791de;
    --text-on-blue: #ffffff;
    --tagline: #7cc3f0;
  }
  * { margin: 0; padding: 0; box-sizing: border-box; }
  html, body {
    width: 1200px; height: 421px; overflow: hidden;
    background: var(--page-bg);
  }
  .canvas {
    position: relative; width: 1200px; height: 421px;
    border: 1px solid var(--page-border);
    font-family: "Roboto", Arial, sans-serif;
  }
  .card { position: absolute; top: 52px; width: 482px; height: 302px; }

  /* front */
  .card-front {
    left: 101px; background: #fff; border: 1px solid var(--card-border);
  }
  .front-brand {
    position: absolute; left: 104px; top: 120px;
    display: flex; align-items: center; gap: 18px;
  }
  .brand-square { width: 58px; height: 58px; background: var(--brand-blue); }
  .brand-name {
    font-family: "Oswald", "Arial Narrow", sans-serif; font-weight: 500;
    color: var(--ink); line-height: 1; letter-spacing: 2px;
  }
  .front-brand .brand-name { font-size: 56px; }
  .front-brand .brand-name span { display: block; font-size: 40px; letter-spacing: 6px; margin-top: 8px; }

  /* back */
  .card-back { left: 609px; background: var(--panel-light); overflow: hidden; }
  .back-panel {
    position: absolute; left: 0; top: 0; width: 280px; height: 100%;
    background: var(--panel-dark);
  }
  .back-panel::after {
    content: ""; position: absolute; right: -9px; top: 140px;
    border-top: 9px solid transparent; border-bottom: 9px solid transparent;
    border-left: 9px solid var(--panel-dark);
  }
  .back-brand {
    position: absolute; left: 30px; top: 22px;
    display: flex; align-items: center; gap: 8px;
  }
  .back-brand .brand-square { width: 18px; height: 18px; background: var(--text-on-blue); }
  .back-brand .brand-name { color: var(--text-on-blue); font-size: 16px; letter-spacing: 1px; }
  .back-brand .brand-name span { display: block; font-size: 12px; letter-spacing: 3px; margin-top: 2px; }

  .person { position: absolute; left: 58px; top: 131px; color: var(--text-on-blue); }
  .person-name { font-size: 17px; font-weight: 500; }
  .person-role { font-size: 15px; margin-top: 3px; }

  .tagline {
    position: absolute; left: 58px; top: 266px;
    font-family: "Oswald", "Arial Narrow", sans-serif; font-size: 10px;
    letter-spacing: 1.2px; color: var(--tagline);
  }

  .contact { position: absolute; left: 304px; color: var(--text-on-blue); font-size: 11.5px; line-height: 18px; }
  .contact b { font-weight: 500; margin-right: 6px; }
  .contact-top { top: 34px; }
  .contact-email { top: 140px; }
</style>
</head>
<body>
<div class="canvas">
  <section class="card card-front">
    <div class="front-brand">
      <div class="brand-square"></div>
      <div class="brand-name">TOLVEN<span>PAINTING</span></div>
    </div>
  </section>

  <section class="card card-back">
    <div class="back-panel">
      <div class="back-brand">
        <div class="brand-square"></div>
        <div class="brand-name">TOLVEN<span>PAINTING</span></div>
      </div>
      <div class="person">
        <div class="person-name">Jonas Tolven</div>
        <div class="person-role">Managing Director</div>
      </div>
      <div class="tagline">DOMESTIC, RESIDENTIAL &amp; COMMERCIAL</div>
    </div>
    <div class="contact contact-top">
      <div><b>M</b>0400 555 193</div>
      <div><b>ABN</b>: 51 300 712 468</div>
    </div>
    <div class="contact contact-email">
      <div><b>E</b>tolvenpainting@example.com</div>
    </div>
  </section>
</div>
</body>
</html>
```